We are in search of a new business card design for our business. We have a Mexican Grocery Store called Tortilla Grove Market, we would like to see that some have mexican design, but we are open to any type of designs.

Phone: to be announced
Fax: to be announced

Address is:
2415 Calloway Blvd
Edgemere, MD 21219

```html
<!DOCTYPE html>
<html lang="en">
<head>
<meta charset="utf-8">
<title>Tortilla Grove Market — Business Card</title>
<link rel="stylesheet" href="https://fonts.googleapis.com/css2?family=Open+Sans:wght@400;600;700;800&display=swap">
<style>
  :root {
    --backdrop: #e7e4df;
    --card-frost: #f5f4f2;
    --card-edge: #c9c6c1;
    --band-red: #b01f24;
    --band-deep: #6e0f14;
    --band-glow: #d23a3a;
    --gold: #f2b431;
    --gold-dark: #c58d1c;
    --pepper-green: #2f7d2a;
    --arc-white: #ffffff;
    --text-light: #f3e9e4;
    --brand-red: #8e1b1e;
  }
  * { box-sizing: border-box; margin: 0; padding: 0; }
  html, body {
    width: 1200px;
    height: 969px;
    overflow: hidden;
    background: var(--backdrop);
    font-family: "Open Sans", Arial, sans-serif;
  }
  .canvas { position: relative; width: 1200px; height: 969px; }
  .card {
    position: absolute;
    left: 393px;
    top: 128px;
    width: 405px;
    height: 712px;
    background: var(--card-frost);
    border: 1px solid var(--card-edge);
    overflow: hidden;
  }
  .card-band { position: absolute; left: 0; top: 0; width: 405px; height: 712px; }
  .brand {
    position: absolute;
    left: 0;
    right: 0;
    top: 110px;
    text-align: center;
    color: var(--brand-red);
    font-weight: 800;
    font-size: 38px;
    line-height: 42px;
  }
  .contact-row {
    position: absolute;
    left: 42px;
    width: 315px;
    text-align: center;
    color: var(--text-light);
    white-space: nowrap;
  }
  .contact-icon { display: block; margin: 0 auto; fill: var(--gold); }
  .person-icon { top: 333px; }
  .person-name {
    top: 376px;
    color: var(--gold);
    font-weight: 600;
    font-size: 24px;
    line-height: 30px;
    letter-spacing: 0.5px;
  }
  .person-title { top: 406px; font-size: 18px; line-height: 24px; letter-spacing: 0.5px; }
  .phone-icon { top: 449px; }
  .phone-line { top: 472px; font-size: 18px; line-height: 26px; }
  .fax-icon { top: 509px; }
  .fax-line { top: 528px; font-size: 18px; line-height: 26px; }
  .pin-icon { top: 575px; }
  .address-line { font-size: 19px; line-height: 28px; }
  .address-street { top: 603px; }
  .address-city { top: 632px; }
</style>
</head>
<body>
<div class="canvas">
  <div class="card">
    <svg class="card-band" viewBox="0 0 405 712" aria-hidden="true">
      <defs>
        <radialGradient id="bandFill" cx="0.35" cy="0.5" r="0.75">
          <stop offset="0" stop-color="var(--band-glow)"/>
          <stop offset="0.55" stop-color="var(--band-red)"/>
          <stop offset="1" stop-color="var(--band-deep)"/>
        </radialGradient>
      </defs>
      <path d="M42 242 Q190 312 357 218 L357 712 L42 712 Z" fill="url(#bandFill)"/>
      <path d="M36 238 Q190 318 364 212" fill="none" stroke="var(--arc-white)" stroke-width="6"/>
      <line x1="47" y1="250" x2="47" y2="712" stroke="var(--gold)" stroke-width="3"/>
      <line x1="355" y1="224" x2="355" y2="712" stroke="var(--pepper-green)" stroke-width="3"/>
    </svg>

    <div class="brand">Tortilla Grove<br>Market</div>

    <div class="contact-row person-icon">
      <svg class="contact-icon" width="28" height="30" viewBox="0 0 30 32" aria-hidden="true">
        <circle cx="15" cy="9" r="8"/>
        <path d="M1 32 Q1 19 15 19 Q29 19 29 32 Z"/>
      </svg>
    </div>
    <div class="contact-row person-name">MARCO REYES</div>
    <div class="contact-row person-title">CEO/FOUNDER</div>

    <div class="contact-row phone-icon">
      <svg class="contact-icon" width="17" height="17" viewBox="0 0 24 24" aria-hidden="true">
        <path d="M6.6 10.8a15.2 15.2 0 0 0 6.6 6.6l2.2-2.2a1 1 0 0 1 1-.25 11.4 11.4 0 0 0 3.6.57 1 1 0 0 1 1 1V20a1 1 0 0 1-1 1A17 17 0 0 1 3 4a1 1 0 0 1 1-1h3.5a1 1 0 0 1 1 1c0 1.25.2 2.45.57 3.57a1 1 0 0 1-.25 1z"/>
      </svg>
    </div>
    <div class="contact-row phone-line">410 555 0187</div>

    <div class="contact-row fax-icon">
      <svg class="contact-icon" width="21" height="17" viewBox="0 0 22 18" aria-hidden="true">
        <rect x="5" y="0" width="12" height="6" rx="1"/>
        <rect x="0" y="6" width="22" height="8" rx="2"/>
        <rect x="5" y="11" width="12" height="7" rx="1" fill="var(--gold-dark)"/>
      </svg>
    </div>
    <div class="contact-row fax-line">410 555 0243</div>

    <div class="contact-row pin-icon">
      <svg class="contact-icon" width="19" height="26" viewBox="0 0 20 28" aria-hidden="true">
        <path d="M10 0a10 10 0 0 0-10 10c0 7.5 10 18 10 18s10-10.5 10-18A10 10 0 0 0 10 0zm0 14a4 4 0 1 1 0-8 4 4 0 0 1 0 8z"/>
      </svg>
    </div>
    <div class="contact-row address-line address-street">2415 Calloway Blvd</div>
    <div class="contact-row address-line address-city">Edgemere, MD 21219</div>
  </div>
</div>
</body>
</html>
```